Kem7Dex Letterhead

Need a new letterhead for my law firm.
IDENTIFYING INFORMATION BELOW:
Ansel T Brightwater III
Attorney at Law
Address: 4832 Tillbury Rd, Ste 250, Dallas, TX 75204
Phone: 866-402-7183
Fax: 469-583-0271
Email: kem@kem7dex.example
Website: www.kem7dex.example

Colors
0054AA
0677BA
7BADD7
CADEEF
E8F1F8

Requirements
Must have
• Logo needs to be on the letterhead, along with identifying information which is included in the project description.

```html
<!DOCTYPE html>
<html lang="en">
<head>
<meta charset="utf-8">
<title>Kem7Dex Letterhead</title>
<link href="https://fonts.googleapis.com/css2?family=Figtree:wght@400;500;700&display=swap" rel="stylesheet">
<style>
  :root{
    --backdrop:#e2e2e2;
    --paper:#ffffff;
    --ink:#1d1d1f;
    --ink-soft:#333336;
    --brand-deep:#0054AA;
    --brand-mid:#0677BA;
    --brand-light:#12a6e0;
    --signature-fill:#ececee;
  }
  *{box-sizing:border-box;margin:0;padding:0}
  html,body{width:1200px;height:1200px;overflow:hidden}
  body{background:var(--backdrop);font-family:"Figtree",sans-serif;color:var(--ink);position:relative}
  .letterhead{position:absolute;left:204px;top:40px;width:792px;height:1120px;background:var(--paper);box-shadow:0 2px 10px rgba(0,0,0,.08)}
  .brand{position:absolute;top:58px;left:0;right:0;text-align:center}
  .brand-name{font-family:"Figtree",sans-serif;font-weight:700;font-size:54px;line-height:1;color:var(--ink)}
  .recipient{position:absolute;left:74px;top:232px;font-size:16px;line-height:21.4px;color:var(--ink-soft);font-style:normal}
  .salutation{position:absolute;left:74px;top:381px;font-size:16px;color:var(--ink-soft)}
  .letter-body{position:absolute;left:74px;top:423px;width:643px;font-size:16px;line-height:21.4px;text-align:justify;color:var(--ink-soft)}
  .signature{position:absolute;left:247px;top:929px;width:299px;height:53px;background:var(--signature-fill);border-radius:4px}
  .signer{position:absolute;left:0;right:0;top:986px;text-align:center}
  .signer-name{font-weight:700;font-size:13.5px;letter-spacing:.12em;color:var(--brand-mid);text-transform:uppercase}
  .signer-title{margin-top:3px;font-size:9.5px;letter-spacing:.16em;color:var(--ink);text-transform:uppercase}
  .footer-rule{position:absolute;left:113px;width:566px;top:1026px;border-top:1.5px solid var(--ink)}
  .footer-address{position:absolute;left:0;right:0;top:1034px;text-align:center;font-weight:500;font-size:15px;color:var(--ink)}
  .footer-contacts{position:absolute;left:0;right:0;top:1060px;display:flex;justify-content:center;gap:10px;font-size:11.5px;color:var(--ink)}
  .contact{display:flex;align-items:center;gap:3px}
  .contact svg{width:10px;height:10px;fill:none;stroke:var(--brand-mid);stroke-width:1.6}
  .footer-band{position:absolute;left:0;right:0;bottom:0;height:23px;background:linear-gradient(90deg,var(--brand-deep) 0%,var(--brand-mid) 25%,var(--brand-light) 50%,var(--brand-mid) 75%,var(--brand-deep) 100%)}
</style>
</head>
<body>
<main class="letterhead">
  <header class="brand">
    <div class="brand-name">Kem7Dex</div>
  </header>

  <address class="recipient">
    Mr. John Doe<br>President<br>Strategy Accountants<br>111 Street Name,<br>City State, 12345
  </address>

  <p class="salutation">Dear</p>

  <div class="letter-body">
    <p>Lorem ipsum dolor sit amet, consectetur adipiscing elit. Aenean ut ipsum eget massa hendrerit vestibulum vel in velit. Donec pretium neque velit.</p>
    <p>Aliquam porta lectus nec mauris ornare venenatis. Vivamus non est turpis, et cursus sem. Mauris vehicula erat in diam auctor at bibendum nisl lacinia.</p>
    <p>Morbi imperdiet neque vehicula nunc convallis gravida. Vestibulum iaculis pretium placerat. Integer consequat, est sit amet facilisis eleifend, nibh nibh varius orci, eget dapibus arcu dui non purus. Pellentesque in magna mauris. Duis enim sapien, dictum vitae condimentum a, pulvinar vel lacus. Mauris et molestie nibh. Vestibulum vitae nulla at metus elementum porta sit amet interdum elit. Nulla sollicitudin neque eu nulla volutpat congue.</p>
    <p>Etiam pellentesque, velit id dapibus fermentum, turpis sapien ornare dui, ac tincidunt ligula odio congue purus. Nunc sed ante dui, in porta lectus. Cras nec sem lorem. In hac habitasse platea dictumst. Maecenas id diam quis dui porta tristique. Sed id egestas felis. Donec ullamcorper mattis posuere. Phasellus fermentum eleifend tortor vel dapibus. Vestibulum ante ipsum.</p>
  </div>

  <div class="signature" role="img" aria-label="Handwritten signature of Ansel T Brightwater III"></div>

  <div class="signer">
    <div class="signer-name">Ansel T Brightwater III</div>
    <div class="signer-title">Attorney at Law</div>
  </div>

  <div class="footer-rule"></div>
  <div class="footer-address">4832 Tillbury Rd, Ste 250, Dallas, TX 75204</div>
  <div class="footer-contacts">
    <span class="contact"><svg viewBox="0 0 12 12"><path d="M2 1.5l2 0 1 2.5-1.2 1a6 6 0 0 0 3.2 3.2l1-1.2 2.5 1v2a1 1 0 0 1-1 1A9 9 0 0 1 1 2.5a1 1 0 0 1 1-1z"/></svg>866-402-7183</span>
    <span class="contact"><svg viewBox="0 0 12 12"><rect x="2" y="5" width="8" height="5" rx="1"/><path d="M3.5 5V1.5h5V5M4 7.5h4"/></svg>469-583-0271</span>
    <span class="contact"><svg viewBox="0 0 12 12"><rect x="1.5" y="3" width="9" height="6.5" rx="1"/><path d="M1.5 3.5L6 7l4.5-3.5"/></svg>kem@kem7dex.example</span>
    <span class="contact"><svg viewBox="0 0 12 12"><circle cx="6" cy="6" r="4.5"/><path d="M1.5 6h9M6 1.5c-2 2.5-2 6.5 0 9M6 1.5c2 2.5 2 6.5 0 9"/></svg>www.kem7dex.example</span>
  </div>

  <div class="footer-band"></div>
</main>
</body>
</html>
```